Positive Psychology and Coaching Web Design Project

I am a trained psychologist and need to develop a website for my positive life coaching and positive psychology training business. My business is based on Positive Psychology, which is the science of human performance enhancement, to help people reach their potential and flourish in their lives. I work with both individuals, and groups in both businesses and schools helping people improve and create more positive, authentic and successful lives by enhancing their performance and improving their wellbeing, resilience, happiness and quality of life.
The business name: My company is named after a fruit, the pomegranate, which is a very special super fruit, with health enhancing benefits and it is a symbol for growth and positive relationships. The pomegranate is full of many seeds, which represent potential, possibilities and ideas.
The website should have integrity, be professional, strong, inspiring and authentic.

Target Market(s)

I coach and work with executives, individuals and children one-on-one, and also teach and train groups in both businesses and schools. The website needs to be professional, in order to fit into the corporate world of executive coaching, but also friendly and inspiring to fit in with positive education in schools.

Industry/Entity Type

Life Coaching

Font styles to use
Sans Serif

Requirements
Must have
• Use of my logo, however, it is flexible how it is used, and the designer can choose which version to use. There is a closed pomegranate with leaves, an open pomegranate to show seeds with leaves, and both of these without leaves.
See attached files:
File 1: A.png: preferred version used on back of business card
File 4: B.png: preferred version but not used anywhere yet, but goes nicely with A?
File 3: C.png: open pomegranate with seeds used on text side of business card
File 2: D.png: plain pomegranate, could be used as a bullet point??!

A home page with toggle buttons to go to other pages such as:
Home
About
Individuals & Organisations
Young People & Schools
Resources
Contact
Nice to have
• The pomegranate is full of many seeds, which represent potential, possibilities and ideas. My logo has a version with the closed pomegranate, and one with the open pomegranate revealing the seeds. Both these could be used on the website, perhaps clicking on the closed pomegranate to reveal the seeds??! My business card has the closed pomegranate on the back and the open seed pomegranate on the side with my name and details. I trust the designer to choose professional suitable colours, however, I do like the colours used on my logo and business card and the consistency might be nice, these colours are:
Pomegranate Red Colour C:24.67%, M: 100%, Y: 100%, K: 24.49%;
Green Writing Colour: C: 71.16%, M: 49.66%, Y: 100%, K: 54.04%
Green Leaf Colour: C: 69.18%, M: 47.02%, Y: 100%, K: 48.21%

```html
<!DOCTYPE html>
<html lang="en">
<head>
<meta charset="utf-8">
<title>Seedwell Coaching – Positive Psychology &amp; Life Coaching</title>
<link rel="stylesheet" href="https://fonts.googleapis.com/css2?family=Didact+Gothic&family=Mulish:wght@600;700;800&display=swap">
<style>
  :root {
    --red: #9b1b1f;
    --red-text: #9a1114;
    --green: #5b6a0a;
    --ink: #3d3d3d;
    --muted: #7a7a7a;
    --rule: #dcdcdc;
    --page-grey: #ebe9e6;
    --white: #ffffff;
    --black: #111111;
    --body: "Didact Gothic", "Century Gothic", sans-serif;
    --heading: "Mulish", "Century Gothic", sans-serif;
  }
  * { box-sizing: border-box; margin: 0; padding: 0; }
  html, body { width: 904px; height: 1200px; overflow: hidden; }
  body { position: relative; background: var(--white); font-family: var(--body); color: var(--ink); }

  .site-header { position: absolute; top: 0; left: 0; width: 904px; height: 119px; border-top: 3px solid var(--red); }
  .brand { position: absolute; left: 68px; top: 36px; display: flex; align-items: center; gap: 12px; }
  .brand-dot { width: 44px; height: 44px; border-radius: 50%; background: var(--red); }
  .brand-name { font-family: var(--heading); font-weight: 700; font-size: 25px; color: var(--red); letter-spacing: -0.3px; }
  .contact-block { position: absolute; right: 62px; top: 28px; width: 160px; text-align: right; font-family: var(--heading); font-weight: 700; font-size: 11.5px; color: var(--ink); line-height: 17px; }
  .contact-block .email { margin-top: 6px; padding-top: 5px; border-top: 1px solid var(--rule); }

  .main-nav { position: absolute; top: 119px; left: 0; width: 904px; height: 45px; background: var(--red); }
  .main-nav ul { list-style: none; display: flex; margin-left: 52px; height: 45px; }
  .main-nav a { display: block; height: 45px; line-height: 45px; padding: 0 16px 0 15px; margin-right: 4px; color: var(--white); text-decoration: none; font-family: var(--heading); font-weight: 700; font-size: 14px; }
  .main-nav a.is-current { background: var(--black); }

  .hero-band { position: absolute; top: 164px; left: 0; width: 904px; height: 295px; background: var(--page-grey); }
  .hero-card { position: absolute; left: 52px; top: 24px; width: 800px; height: 248px; background: var(--white); }
  .hero-photo { position: absolute; left: 0; top: 0; width: 445px; height: 248px;
    background: linear-gradient(90deg, #e6b285 0%, #f1c9a3 35%, #f8dfc6 70%, #ffffff 100%); }
  .hero-copy { position: absolute; left: 432px; top: 24px; width: 340px; }

  h2 { font-family: var(--heading); font-weight: 800; color: var(--red-text); font-size: 19.5px; line-height: 24px; }
  .rule { height: 1px; background: var(--rule); }
  .hero-copy .rule { margin: 10px 0 16px; }
  .hero-copy p { font-size: 14.5px; line-height: 19.3px; }

  .button { display: inline-block; background: var(--green); color: var(--white); font-size: 14.5px; text-align: center; width: 138px; height: 35px; line-height: 35px; text-decoration: none; }
  .hero-copy .button { margin-top: 18px; margin-left: 2px; }

  .programs { position: absolute; top: 459px; left: 0; width: 904px; height: 296px; background: var(--white); display: flex; padding-left: 42px; }
  .program { width: 275px; text-align: center; padding-top: 24px; }
  .program-icon { display: block; margin: 0 auto; width: 56px; height: 56px; }
  .program h3 { font-family: var(--heading); font-weight: 800; color: var(--red-text); font-size: 19.5px; line-height: 19.5px; margin-top: 17px; }
  .program .rule { width: 212px; margin: 14px auto 15px; }
  .program p { font-size: 14.5px; line-height: 18px; padding: 0 24px; }
  .program .button { margin-top: 16px; }

  .content-band { position: absolute; top: 755px; left: 0; width: 904px; height: 347px; background: var(--page-grey); }
  .panel { position: absolute; background: var(--white); top: 24px; }
  .about-panel { left: 52px; width: 526px; height: 267px; padding: 22px 26px 0; }
  .about-panel .rule { margin: 12px 0 14px; }
  .about-panel p { font-size: 14.5px; line-height: 19.3px; padding-left: 1px; margin-bottom: 14px; }
  .news-panel { left: 602px; width: 250px; height: 250px; padding: 22px 24px 0; }
  .news-panel .rule { margin: 11px 0 16px; }
  .news-date { font-size: 12px; color: var(--muted); margin-bottom: 10px; padding-left: 1px; }
  .news-panel p { font-size: 14.5px; line-height: 19.3px; padding-left: 1px; }
  .text-link { display: inline-block; color: var(--red-text); font-size: 14.5px; text-decoration: underline; text-underline-offset: 3px; margin-top: 4px; }
  .news-panel .text-link { margin-top: 14px; }

  .site-footer { position: absolute; top: 1102px; left: 0; width: 904px; height: 98px; text-align: center; }
  .footer-nav { list-style: none; display: flex; justify-content: center; margin-top: 28px; font-size: 12px; }
  .footer-nav li { color: var(--red-text); }
  .footer-nav li + li::before { content: "|"; margin: 0 17px; }
  .footer-nav a { color: var(--red-text); text-decoration: none; }
  .footer-note { font-size: 11.5px; margin-top: 16px; color: var(--ink); }
</style>
</head>
<body>
  <header class="site-header">
    <div class="brand">
      <span class="brand-dot"></span>
      <span class="brand-name">Seedwell Coaching</span>
    </div>
    <div class="contact-block">
      <div>Call us:</div>
      <div>1800-555-017</div>
      <div class="email">hello@seedwellcoaching.com.au</div>
    </div>
  </header>

  <nav class="main-nav">
    <ul>
      <li><a class="is-current" href="#">Home</a></li>
      <li><a href="#">About</a></li>
      <li><a href="#">Individuals &amp; Organisations</a></li>
      <li><a href="#">Young People &amp; Schools</a></li>
      <li><a href="#">Resources</a></li>
      <li><a href="#">Contact</a></li>
    </ul>
  </nav>

  <section class="hero-band">
    <div class="hero-card">
      <div class="hero-photo" role="img" aria-label="Portrait photograph of the coach against a warm peach backdrop"></div>
      <div class="hero-copy">
        <h2>Positive Psychology &amp; Life Coaching</h2>
        <div class="rule"></div>
        <p>Lorem ipsum dolor sit amet, consectetur adipiscing elit. Donec est leo, viverra eget risus ac, euismod elementum odio. Cras turpis velit, vestibulum et sagittis sed, accumsan a est. Donec massa quam, facilisis eget vulputate nec.</p>
        <a class="button" href="#">Lorem ipsum</a>
      </div>
    </div>
  </section>

  <section class="programs">
    <article class="program">
      <svg class="program-icon" viewBox="0 0 56 56" aria-hidden="true"><circle cx="28" cy="28" r="27" fill="var(--red)"/></svg>
      <h3>Programs for Individuals and Organisations</h3>
      <div class="rule"></div>
      <p>Lorem ipsum dolor sit amet, consectetur adipiscing elit. Nulla sed ipsum pulvinar.</p>
      <a class="button" href="#">Lorem ipsum</a>
    </article>
    <article class="program">
      <svg class="program-icon" viewBox="0 0 56 56" aria-hidden="true"><circle cx="28" cy="28" r="27" fill="var(--red)"/></svg>
      <h3>Programs for Schools and Young People</h3>
      <div class="rule"></div>
      <p>Lorem ipsum dolor sit amet, consectetur adipiscing elit. Nulla sed ipsum pulvinar.</p>
      <a class="button" href="#">Lorem ipsum</a>
    </article>
    <article class="program">
      <svg class="program-icon" viewBox="0 0 56 56" aria-hidden="true"><circle cx="28" cy="28" r="27" fill="var(--red)"/></svg>
      <h3>Other Programs and Resources</h3>
      <div class="rule"></div>
      <p>Lorem ipsum dolor sit amet, consectetur adipiscing elit. Nulla sed ipsum pulvinar.</p>
      <a class="button" href="#">Lorem ipsum</a>
    </article>
  </section>

  <section class="content-band">
    <article class="panel about-panel">
      <h2>Positive Psychology &amp; Life Coaching</h2>
      <div class="rule"></div>
      <p>The science of human performance enhancement, to help people reach their potential and flourish in their lives.</p>
      <p>I work with both individuals, and groups in both businesses and schools helping people improve and create more positive, authentic and successful lives by enhancing their performance and improving their wellbeing, resilience, happiness and quality of life.</p>
      <a class="text-link" href="#">Learn more about our approach</a>
    </article>
    <aside class="panel news-panel">
      <h2>Latest News</h2>
      <div class="rule"></div>
      <div class="news-date">Posted on: 2 Jun, 2015</div>
      <p>Nullam fringilla enim eget sem ultricies, et aliquam libero lacinia. Praesent tortor erat, pharetra quis tellus id, scelerisque dapibus dui. [...]</p>
      <a class="text-link" href="#">Read more</a>
    </aside>
  </section>

  <footer class="site-footer">
    <ul class="footer-nav">
      <li><a href="#">Home</a></li>
      <li><a href="#">About</a></li>
      <li><a href="#">Individuals &amp; Organisations</a></li>
      <li><a href="#">Young People &amp; Schools</a></li>
      <li><a href="#">Resources</a></li>
      <li><a href="#">Contact</a></li>
    </ul>
    <p class="footer-note">Lorem ipsum dolor sit amet, consectetur adipiscing elit.</p>
  </footer>
</body>
</html>
```